Tallow Roost Lead Generator + Checklist

I have typed up a 9 page word doc to be a lead generator for my website called "6 Simple Secrets Gala Hosts Love" and I am looking for someone to clean it up, and make it professional and inline with our brand.

Logo Hex: #971F20

Industry/Entity Type

Event Planning

Font styles to use
Other font styles liked:
• Helvetica Neue is our brands font, but it doesn't have to be that. Something similar that is rounded would be good like Arial I think.

Requirements
Must have
• Clean, but elegant design.
• Because it is very text heavy, have the topics easily broken out and maybe staggered so that it is easy to identify main topics and sub topics.
Should not have
• Not just looking for basic formating around the edges of the document, but to also have the text displayed in an easily readable way with clear sections.

```html
<!DOCTYPE html>
<html lang="en">
<head>
<meta charset="utf-8">
<title>Tallow Roost – 6 Simple Secrets Gala Hosts Love</title>
<link rel="stylesheet" href="https://fonts.googleapis.com/css2?family=Inter:wght@100;400;700&display=swap">
<style>
  :root {
    --brand-red: #971f20;
    --ink: #1a1a1a;
    --numeral: #e4e4e6;
    --paper: #ffffff;
  }
  * { box-sizing: border-box; margin: 0; padding: 0; }
  html, body { width: 1200px; height: 777px; overflow: hidden; background: var(--paper); }
  body { font-family: "Inter", "Helvetica Neue", Arial, sans-serif; color: var(--ink); }
  .spread { position: relative; width: 1200px; height: 777px; overflow: hidden; }
  .page-numeral {
    position: absolute; font-weight: 100; color: var(--numeral);
    font-size: 330px; line-height: 1; z-index: 0; letter-spacing: -10px;
  }
  .page-numeral.four { left: 14px; top: 548px; }
  .page-numeral.five { left: 618px; top: 548px; }
  .section { position: absolute; top: 55px; width: 524px; z-index: 1; }
  .section.left { left: 34px; }
  .section.right { left: 642px; }
  .section-title {
    background: var(--brand-red); color: #fff; font-weight: 700;
    font-size: 14.2px; line-height: 17px; padding: 2px 10px 2px 37px;
    position: relative; letter-spacing: -0.1px;
  }
  .section-title .num { position: absolute; left: 10px; }
  .section-body { padding: 8px 0 0 37px; }
  .lead {
    font-weight: 700; font-size: 13.4px; line-height: 16px; letter-spacing: -0.1px;
  }
  .steps { list-style: none; margin: 7px 0 8px 0; }
  .steps li {
    position: relative; padding-left: 46px; font-size: 11.1px; line-height: 13.6px;
    margin-bottom: 5px; padding-right: 0;
  }
  .steps .n { position: absolute; left: 23px; color: var(--brand-red); font-weight: 700; }
  .steps strong { font-weight: 700; }
  .footer { position: absolute; top: 741px; font-size: 7.4px; display: flex; align-items: center; gap: 5px; z-index: 1; }
  .footer.left { left: 14px; }
  .footer.right { right: 14px; }
  .footer .page-no { color: var(--brand-red); font-weight: 700; }
  .footer .mark { width: 13px; height: 13px; background: var(--brand-red); display: inline-block; }
</style>
</head>
<body>
<main class="spread">
  <div class="page-numeral four" aria-hidden="true">4</div>
  <div class="page-numeral five" aria-hidden="true">5</div>

  <section class="section left">
    <h2 class="section-title"><span class="num">4.</span>Plan the food and drinks - that’s why everyone is coming in the first place</h2>
    <div class="section-body">
      <p class="lead">We’ve all been to those events where there isn’t enough food, or the food is cold and the drinks are warm - you definitely don’t want to be planning the event where people leave early to go to a drive through on the way home.</p>
      <ol class="steps">
        <li><span class="n">1.</span><strong>Have a Plan -</strong> Have basic questions answered such as what food will be served, when will it be served or how can it be ordered, if there will be a private bar just for your group or if guests need to go to a public bar.</li>
        <li><span class="n">2.</span><strong>Caterer Coordination -</strong> All of this is even more important if you have a caterer or are bringing in outside food which typically requires a higher level of coordination than if the venue provides the food. Also - before you start looking into outside caterers or bringing you own food, make sure you check with the venue to see what their requirements are for outside caterers. Many venues have a short list of caterers they allow or they require certain documentation.</li>
      </ol>
      <p class="lead">Ensuring that the food and drink details are nailed down is a must. After all, if everyone is having a good time - some other minor details that may have been missed will probably be quickly forgotten by the next day. On the other hand, if people aren’t having a good time - they are only going to remember problems more clearly!</p>
    </div>
  </section>

  <section class="section right">
    <h2 class="section-title"><span class="num">5.</span>Lastly, Don’t take anything for granted.</h2>
    <div class="section-body">
      <p class="lead">Even after the ‘heavy lifting’ is done and you’ve found your venue and have any necessary vendors lined up, don’t just kick back and wait for the event to happen. Remember, great events don’t just happen - they happen because the planner commits to planning a great event.</p>
      <ol class="steps">
        <li><span class="n">1.</span><strong>Confirm Venue and Vendors -</strong> Depending on the complexity of the event, make sure to follow up with the venue and vendors about a month beforehand, a week beforehand and the day before to make sure that everything is set, and no unexpected issues have come up at the last minute (vendors being sick, running out of supplies, etc) that may derail the event.</li>
        <li><span class="n">2.</span><strong>Communicate with Guests -</strong> Guests can often require a similar level of detail. Sending out a reminder with basic information a week before and the day before is a good way to reduce no-shows and last minute calls and texts from people at the venue who can’t find the room, parking, etc. Tools like Inkwell Invites, Ticketloom or a Gatherly Event make this a breeze.</li>
        <li><span class="n">3.</span><strong>Signage -</strong> Clear and simple signs on the day of an event are usually great for any venue, especially if they have multiple rooms or the private event room is on a different floor or in the back of the venue.</li>
        <li><span class="n">4.</span><strong>“Day of” Box -</strong> Again, it depends on the type and complexity of the event, but it is good to start collecting everything you’ll need for the event a day or two beforehand in one place. Programs, Signs, Easels, Pens, Nametags, Wireless slide advancers, Speaker gifts, Scripts, Adapter cables for laptops and projectors, etc so that when the time comes you can easily ensure everything is in one place and it will give you time to run to Deskmart or Harlow Mart the day before the event, as opposed to realizing you’re missing something during setup on the day of the event.</li>
        <li><span class="n">5.</span><strong>“Day of” Checklist -</strong> If the event isn’t an event you do every week, I’d highly recommend developing a simple ‘day of’ checklist that covers everything you need to do, everything you need to bring, etc. for the day of the event. There is simply too much going on to remember everything, and especially if something unexpected happens - it is hard if not impossible to remember to go back and do all of those little, but important tasks. Also if you have a checklist, you can easily delegate other tasks to people and keep track of them in one place.</li>
      </ol>
      <p class="lead">By following through until the end - you’ll ensure that your event is a success from start to finish. Although you’ll have put some more work upfront as opposed to just ‘winging it’ your investment will pay dividends. While someone else is scrambling around at the last minute to find a new venue because they overlooked a key detail that is a show stopper, or wondering why less people than expected showed up, you will rest easy knowing that your event is at the perfect venue, that all of the details have been accounted for and that you’ll be relaxing and enjoying the event, rather than running around putting out fires.</p>
    </div>
  </section>

  <footer class="footer left"><span class="mark" aria-hidden="true"></span><span><span class="page-no">6</span> | Tallow Roost</span></footer>
  <footer class="footer right"><span>6 Simple Secrets Gala Hosts Love | <span class="page-no">7</span></span><span class="mark" aria-hidden="true"></span></footer>
</main>
</body>
</html>
```